Progressive Architecture and Urban Planning Studio - Stationery Design

The Kestrel Collective: a small boutique Architectural and Urban Planning Studio based in Natal/ RN, Brazil, about to open branches in South Africa and West Africa, established to provide high quality, innovative design and personal client service for projects worldwide. Our approach to Architecture: Minimal - Less is More, so to speak, but with an edge! Strive to produce "clean" projects - stripped of all that can be stripped, no excesses. Got our Logo right here with Pixel Harbor, and hope to do the same with our stationery (were informed that includes business cards, letterhead and envelopes). Since we'll be using two clour schemes, we want at least one using a black background (business card). We'll also allow manipulation of our logo if it helps the final design. Good Luck!

Industry/Entity Type

Business

Other font styles liked:
• Nexa

Colors

Designer to choose colors to be used in the design.

Requirements
Must have
• Business Cards/ Letterheads with the following address:
Rua Benedito Sarmento 742, Jardim Aurora, Porto Alvo/SC
Should be able to edit it.

```html
<!DOCTYPE html>
<html lang="en">
<head>
<meta charset="utf-8">
<title>The Kestrel Collective — Stationery</title>
<link rel="stylesheet" href="https://fonts.googleapis.com/css2?family=Montserrat:wght@400;600;700&family=Open+Sans:wght@400;600;700&family=Great+Vibes&display=swap">
<style>
  :root{
    --backdrop:#a8a8a8;
    --paper:#ffffff;
    --ink:#2b2b2b;
    --body-text:#5a5a5a;
    --muted:#7a7a7a;
    --brand-red:#d3242b;
    --card-black:#151515;
    --signature-blue:#2f4f86;
  }
  *{margin:0;padding:0;box-sizing:border-box}
  html,body{width:1200px;height:900px;overflow:hidden;background:var(--backdrop)}
  body{position:relative;font-family:"Open Sans",Arial,sans-serif;color:var(--ink)}

  .sheet{position:absolute;background:var(--paper)}
  .brand{position:absolute;display:flex;align-items:center}
  .brand-square{background:var(--brand-red);flex:none}
  .brand-name{font-family:"Montserrat",Arial,sans-serif;font-weight:400;color:var(--ink);white-space:nowrap;text-transform:uppercase}

  /* Letterhead */
  .letterhead{left:87px;top:140px;width:483px;height:657px}
  .letterhead .brand{left:38px;top:46px}
  .letterhead .brand-square{width:30px;height:30px;margin-right:22px}
  .letterhead .brand-name{font-size:13.5px;letter-spacing:2.6px}
  .letterhead-contact{position:absolute;left:373px;top:38px;border-left:1px solid var(--brand-red);padding-left:8px;height:50px;font-size:5.4px;line-height:7px;color:var(--muted)}
  .letterhead-contact b{color:var(--brand-red)}
  .letterhead-contact .firm{color:var(--ink);font-weight:700;margin-top:5px}
  .letter-body{position:absolute;left:63px;top:172px;width:388px;font-size:8.5px;line-height:11.6px;color:var(--body-text)}
  .letter-body .salutation{font-weight:700;color:var(--ink);margin-bottom:10px}
  .letter-body p{margin-bottom:11px}
  .signature{position:absolute;left:49px;top:492px;font-family:"Great Vibes",cursive;font-size:24px;color:var(--signature-blue)}
  .signer-title{position:absolute;left:51px;top:522px;font-size:8.5px;font-weight:700;color:var(--muted)}
  .letterhead-web{position:absolute;right:40px;bottom:28px;font-size:5.6px;color:var(--muted)}
  .letterhead-web b{color:var(--ink)}

  /* Business card, front */
  .card-front{left:670px;top:145px;width:220px;height:125px}
  .card-front .brand{left:12px;top:15px}
  .card-front .brand-square{width:16px;height:16px;margin-right:10px}
  .card-front .brand-name{font-size:8px;letter-spacing:1.5px}
  .card-contact{position:absolute;left:12px;top:86px;font-size:5.6px;line-height:7.4px;color:var(--muted)}
  .card-contact b{color:var(--brand-red)}
  .card-person{position:absolute;right:14px;top:87px;text-align:right;font-size:5.8px;line-height:7.4px;color:var(--muted)}
  .card-person .person-name{color:var(--brand-red);font-weight:700;letter-spacing:.3px}
  .card-rule{position:absolute;left:12px;right:14px;top:104px;height:1px;background:var(--brand-red)}
  .card-address{position:absolute;left:12px;top:107px;font-size:5.2px;color:var(--muted);white-space:nowrap}
  .card-address b{color:var(--ink)}

  /* Business card, back */
  .card-back{left:908px;top:142px;width:218px;height:128px;background:var(--card-black)}
  .card-back .brand{left:36px;top:60px}
  .card-back .brand-square{width:14px;height:14px;margin-right:10px}
  .card-back .brand-name{color:#fff;font-size:7px;letter-spacing:1.2px}
  .card-back-web{position:absolute;left:105px;top:76px;font-size:5.4px;color:#bdbdbd}
  .card-back-web b{color:#fff}

  /* Envelope */
  .envelope{left:628px;top:422px;width:514px;height:256px}
  .envelope .brand{left:22px;top:23px}
  .envelope .brand-square{width:20px;height:20px;margin-right:12px}
  .envelope .brand-name{font-size:10px;letter-spacing:2px}
  .envelope-rule{position:absolute;left:22px;top:47px;width:232px;height:1px;background:var(--brand-red)}
  .envelope-address{position:absolute;left:22px;top:50px;font-size:5.4px;color:var(--muted);white-space:nowrap}
  .envelope-address b{color:var(--ink)}
</style>
</head>
<body>

<section class="sheet letterhead">
  <div class="brand"><span class="brand-square"></span><span class="brand-name">The Kestrel Collective</span></div>
  <div class="letterhead-contact">
    <div><b>T</b> • 555-210-4478</div>
    <div><b>E</b> • info@kestrelcollective.com</div>
    <div class="firm">The Kestrel Collective</div>
    <div>Rua Benedito Sarmento 742</div>
    <div>Jardim Aurora, Porto Alvo/SC</div>
  </div>
  <div class="letter-body">
    <div class="salutation">Lorem Ipsum,</div>
    <p>Cras mattis consectetur purus sit amet fermentum. Etiam porta sem malesuada magna mollis euismod. Integer posuere erat a ante venenatis dapibus posuere velit aliquet. Cras justo odio, dapibus ac facilisis in, egestas eget quam. Aenean eu leo quam. Pellentesque ornare sem lacinia quam venenatis vestibulum.</p>
    <p>Vivamus sagittis lacus vel augue laoreet rutrum faucibus dolor auctor. Donec sed odio dui. Etiam porta sem malesuada magna mollis euismod. Morbi leo risus, porta ac consectetur ac, vestibulum at eros. Nullam id dolor id nibh ultricies vehicula ut id elit.</p>
    <p>Donec id elit non mi porta gravida at eget metus. Fusce dapibus, tellus ac cursus commodo, tortor mauris condimentum nibh, ut fermentum massa justo sit amet risus. Cras justo odio, dapibus ac facilisis in, egestas eget quam. Cum sociis natoque penatibus et magnis dis parturient montes, nascetur ridiculus mus.</p>
    <p>Cum sociis natoque penatibus et magnis dis parturient montes, nascetur ridiculus mus. Curabitur blandit tempus porttitor. Aenean lacinia bibendum nulla sed consectetur. Lorem ipsum dolor sit amet, consectetur adipiscing elit.</p>
    <p>Cras justo odio, dapibus ac facilisis in, egestas eget quam. Morbi leo risus, porta ac consectetur ac, vestibulum at eros. Duis mollis, est non commodo luctus, nisi erat porttitor ligula, eget lacinia odio sem nec elit. Integer posuere erat a ante venenatis dapibus posuere velit aliquet. Vivamus sagittis lacus vel augue laoreet rutrum faucibus dolor auctor.</p>
  </div>
  <div class="signature">Marco Valente</div>
  <div class="signer-title">Company Director</div>
  <div class="letterhead-web">www.<b>kestrelcollective</b>.com</div>
</section>

<section class="sheet card-front">
  <div class="brand"><span class="brand-square"></span><span class="brand-name">The Kestrel Collective</span></div>
  <div class="card-contact">
    <div><b>T</b> • 555-210-4478</div>
    <div><b>E</b> • marco@kestrelcollective.com</div>
  </div>
  <div class="card-person">
    <div class="person-name">MARCO VALENTE</div>
    <div>President</div>
  </div>
  <div class="card-rule"></div>
  <div class="card-address"><b>The Kestrel Collective</b>, Rua Benedito Sarmento 742, Jardim Aurora, Porto Alvo/SC</div>
</section>

<section class="sheet card-back">
  <div class="brand"><span class="brand-square"></span><span class="brand-name">The Kestrel Collective</span></div>
  <div class="card-back-web">www.<b>kestrelcollective</b>.com</div>
</section>

<section class="sheet envelope">
  <div class="brand"><span class="brand-square"></span><span class="brand-name">The Kestrel Collective</span></div>
  <div class="envelope-rule"></div>
  <div class="envelope-address"><b>The Kestrel Collective</b>, Rua Benedito Sarmento 742, Jardim Aurora, Porto Alvo/SC</div>
</section>

</body>
</html>
```